Business card for Mortgage broker business

I have already had the logo designed and am needing a great looking business card. My business focus is on servicing clients who may not be able to obtain finance through traditional lenders due to bad credit, short term employment or they just don't fit the banks profile. It needs to be professional, trust worthy but also have a caring fell about it.
I have provided files showing the green and black logo, the white logo(on white background so the file looks blank) and also a file with the white logo with a background of leaves that was made up which will probably be used for a website header.

Industry/Entity Type

Finance

Contact Information for Business Card

Marcus Dalby
Managing Director, Accredited Finance Broker(AFB)
Po Box 817, Ashcombe VIC 3952
marcus@kestrelfunding.com.au
www.kestrelfunding.com.au
0438 216 507

Requirements
Nice to have
• I have added a picture of myself as I would like to see some designs with the pic in it, but I'm not sure if I want it on there with the logo's or just the logo's

```html
<!DOCTYPE html>
<html lang="en">
<head>
<meta charset="utf-8">
<title>Kestrel Funding – Business Card</title>
<link href="https://fonts.googleapis.com/css2?family=Questrial&display=swap" rel="stylesheet">
<style>
  :root {
    --backdrop: #b1b1b1;
    --card-white: #f4f4f4;
    --brand-green: #0a6b3c;
    --brand-green-light: #0b7342;
    --band-dark: #111a15;
    --ink: #1c1c1c;
    --white: #ffffff;
  }
  * { margin: 0; padding: 0; box-sizing: border-box; }
  html, body {
    width: 1200px; height: 1050px; overflow: hidden;
    background: var(--backdrop);
    font-family: "Questrial", "Century Gothic", sans-serif;
  }
  .card {
    position: absolute; left: 264px; width: 672px; height: 384px;
    border-radius: 24px; overflow: hidden;
    box-shadow: 0 3px 8px rgba(0,0,0,0.3);
  }
  .card--front {
    top: 110px;
    background: radial-gradient(ellipse at 50% 40%, #ffffff 0%, var(--card-white) 55%, #e2e2e2 100%);
  }
  .card--back {
    top: 574px;
    background: radial-gradient(ellipse at 50% 35%, var(--brand-green-light) 0%, var(--brand-green) 60%, #075c33 100%);
  }
  .portrait {
    position: absolute; left: 0; top: 22px; width: 320px; height: 336px;
    background: linear-gradient(180deg, rgba(236,236,236,0) 0%, #d9d3cf 35%, #8a7468 65%, #2a2b33 100%);
    border-radius: 40% 40% 0 0;
  }
  .wave { position: absolute; left: 0; top: 0; }
  .logo-text {
    position: absolute; color: var(--brand-green);
    line-height: 1; white-space: nowrap;
    display: flex; align-items: center; gap: 10px;
  }
  .logo-dot { width: 10px; height: 10px; border-radius: 50%; background: currentColor; }
  .card--front .logo-text { right: 50px; top: 72px; font-size: 30px; }
  .card--back .logo-text {
    color: var(--white); font-size: 42px;
    left: 50%; top: 50%; transform: translate(-50%, -50%);
  }
  .card--back .logo-dot { width: 13px; height: 13px; }
  .contact { position: absolute; right: 50px; text-align: right; color: var(--ink); font-size: 16px; line-height: 19px; }
  .contact__name { top: 172px; font-size: 21px; line-height: 26px; color: var(--brand-green); }
  .contact__role { top: 197px; }
  .contact__line { display: flex; align-items: center; gap: 10px; }
  .contact__phone { top: 257px; }
  .contact__email { top: 276px; }
  .contact__address { top: 313px; }
  .icon { width: 14px; height: 14px; fill: var(--brand-green); flex: none; }
  .website {
    position: absolute; left: 50px; top: 356px;
    font-size: 16px; color: var(--white); letter-spacing: 0.3px;
  }
</style>
</head>
<body>
  <section class="card card--front">
    <div class="portrait" role="img" aria-label="Portrait photo of Marcus Dalby in a dark suit"></div>

    <svg class="wave" width="672" height="384" viewBox="0 0 672 384" aria-hidden="true">
      <path d="M0,318 C180,312 330,338 430,362 C520,382 600,365 672,318 L672,384 L0,384 Z" fill="var(--band-dark)"/>
      <path d="M0,344 C150,338 260,352 360,370 C460,388 580,380 672,340" fill="none" stroke="#ffffff" stroke-width="2.5" opacity="0.85"/>
      <path d="M0,350 C150,344 260,358 360,376 C460,392 590,384 672,348 L672,384 L0,384 Z" fill="var(--brand-green)"/>
    </svg>

    <div class="logo-text"><span class="logo-dot"></span>Kestrel Funding</div>

    <div class="contact contact__name">Marcus Dalby</div>
    <div class="contact contact__role">Managing Director,<br>Accredited Finance Broker(AFB)</div>

    <div class="contact contact__line contact__phone">
      <span>0438 216 507</span>
      <svg class="icon" viewBox="0 0 24 24" aria-hidden="true"><path d="M6.6 10.8c1.4 2.8 3.8 5.1 6.6 6.6l2.2-2.2c.3-.3.7-.4 1-.2 1.1.4 2.3.6 3.6.6.6 0 1 .4 1 1V20c0 .6-.4 1-1 1C10.6 21 3 13.4 3 4c0-.6.4-1 1-1h3.5c.6 0 1 .4 1 1 0 1.3.2 2.5.6 3.6.1.3 0 .7-.2 1z"/></svg>
    </div>
    <div class="contact contact__line contact__email">
      <span>marcus@kestrelfunding.com.au</span>
      <svg class="icon" viewBox="0 0 24 24" aria-hidden="true"><path d="M2 5h20v14H2z M3.5 6.5 12 13l8.5-6.5" stroke="#fff" stroke-width="1.4" fill="var(--brand-green)"/></svg>
    </div>
    <div class="contact contact__line contact__address"><span>Po Box 817, Ashcombe VIC 3952</span></div>

    <div class="website">www.kestrelfunding.com.au</div>
  </section>

  <section class="card card--back">
    <div class="logo-text"><span class="logo-dot"></span>Kestrel Funding</div>
  </section>
</body>
</html>
```